Home Care company needs letter head branding

Home care company needs a letter head which can be used for all documents the company's clients view. We provided in home care for the elderly. We would like to use our company colors (2785A7, 0A4057 and 34A74D) and should not be too large as we will be using it on more than just a letter head but all documents our clients sign / receive.
Target Market(s)
Professional business
Industry/Entity Type
Health Care
Requirements
Must have
- corporate brand colors

```html
<!DOCTYPE html>
<html lang="en">
<head>
<meta charset="utf-8">
<title>Brightfield Care – Letterhead</title>
<link rel="stylesheet" href="https://fonts.googleapis.com/css2?family=Mulish:wght@600;700;800&display=swap">
<style>
  :root {
    --teal: #2785a7;
    --navy: #0a4057;
    --lime: #b0cf3a;
    --paper: #ffffff;
  }
  * { margin: 0; padding: 0; box-sizing: border-box; }
  html, body { width: 953px; height: 1200px; overflow: hidden; background: var(--paper); }
  .letterhead {
    position: relative;
    width: 953px;
    height: 1200px;
    background: var(--paper);
    font-family: "Mulish", "Century Gothic", sans-serif;
    overflow: hidden;
  }
  .brand {
    position: absolute;
    left: 64px;
    top: 12px;
    display: flex;
    align-items: center;
    gap: 18px;
  }
  .brand-mark {
    width: 104px;
    height: 104px;
    border-radius: 50%;
    background: var(--teal);
  }
  .brand-name {
    font-size: 46px;
    font-weight: 700;
    color: var(--teal);
    letter-spacing: -0.5px;
    white-space: nowrap;
  }
  .contact {
    position: absolute;
    left: 602px;
    top: 11px;
    height: 76px;
    border-left: 3px solid var(--teal);
    padding-left: 19px;
    color: var(--navy);
    font-weight: 800;
  }
  .contact-address {
    font-size: 15.5px;
    line-height: 18px;
    white-space: nowrap;
  }
  .contact-phone {
    margin-top: 10px;
    font-size: 19px;
    line-height: 22px;
  }
  .footer-wave {
    position: absolute;
    left: 0;
    top: 940px;
    width: 953px;
    height: 260px;
  }
  .footer-url {
    position: absolute;
    left: 0;
    width: 953px;
    top: 1147px;
    text-align: center;
    color: var(--paper);
    font-size: 20px;
    font-weight: 700;
    letter-spacing: 4px;
  }
</style>
</head>
<body>
  <div class="letterhead">
    <header class="brand">
      <span class="brand-mark"></span>
      <span class="brand-name">Brightfield Care</span>
    </header>

    <address class="contact" style="font-style:normal">
      <div class="contact-address">2380 Linden Park Ave, Suite 310<br>Rockville MD 20850</div>
      <div class="contact-phone">(301) 555-0142</div>
    </address>

    <svg class="footer-wave" viewBox="0 0 953 260" preserveAspectRatio="none" aria-hidden="true">
      <defs>
        <linearGradient id="lime-fade" x1="0" y1="0" x2="1" y2="0">
          <stop offset="0" stop-color="#b0cf3a" stop-opacity="0.05"/>
          <stop offset="0.4" stop-color="#b0cf3a" stop-opacity="1"/>
          <stop offset="1" stop-color="#b0cf3a"/>
        </linearGradient>
        <linearGradient id="band-fade" x1="0" y1="0" x2="1" y2="0">
          <stop offset="0" stop-color="#2385a7"/>
          <stop offset="0.45" stop-color="#1f7896"/>
          <stop offset="1" stop-color="#0a3c52"/>
        </linearGradient>
      </defs>
      <path d="M0,184 C420,180 820,150 953,4 L953,260 L0,260 Z" fill="url(#lime-fade)"/>
      <path d="M0,192 C440,189 830,164 953,32 L953,260 L0,260 Z" fill="url(#band-fade)"/>
    </svg>

    <footer class="footer-url">www.brightfieldcare.com</footer>
  </div>
</body>
</html>
```